Original business card of a small accounting firm

My firm specializes in accounting and taxes for small businesses. I'm looking for an original and creative business card as a marketing tool to give to prospective clients; however since we are a professional firm the card must also appear professional. I'm uploading a few examples of what I believe may fit my needs. Please feel free to use them as a jumping off point. Lastly, I'm uploading the company logo which I'd like to be the focal point on the back of the card and somewhat incorporated on the front on a smaller scale. I hope my description was helpful.
Target Market(s)
Tax clients and small businesses
Industry/Entity Type
Accounting
Contact Information for Business Card
Gerald Whitcombe
Certified Public Accountant │President
Whitcombe Advisors
T│ (555) 417-2863
Email│GWhitcombe@WhitcombeAdvisors.example
Look and feel
Each slider illustrates characteristics of the customer's brand and the style your logo design should communicate.

```html
<!DOCTYPE html>
<html lang="en">
<head>
<meta charset="utf-8">
<title>Whitcombe Advisors – Business Card</title>
<link rel="stylesheet" href="https://fonts.googleapis.com/css2?family=Arimo:wght@400;700&family=Cinzel:wght@400&display=swap">
<style>
  :root {
    --stage: #1c1c1e;
    --card-white: #f7f7f8;
    --card-black: #0c0c0d;
    --brand-blue: #2f62b8;
    --name-blue: #4a8ad8;
    --ink: #4a4a4e;
    --ink-soft: #7a7a80;
    --silver: #b8b8bc;
    --divider: #c7cbd6;
  }
  * { box-sizing: border-box; margin: 0; padding: 0; }
  html, body { width: 1200px; height: 873px; overflow: hidden; }
  body {
    background: var(--stage);
    font-family: "Arimo", Arial, sans-serif;
    position: relative;
  }
  .card {
    position: absolute;
    top: 282px;
    width: 530px;
    height: 303px;
    border-radius: 3px;
    overflow: hidden;
  }
  .card--front { left: 60px; background: var(--card-white); }
  .card--back  { left: 610px; background: radial-gradient(ellipse at 50% 45%, #26272b 0%, var(--card-black) 70%); }

  /* front */
  .front-brand {
    position: absolute;
    left: 26px; top: 118px;
    width: 222px;
    display: flex; flex-direction: column; align-items: flex-start;
  }
  .brand-name {
    display: flex; align-items: center; gap: 8px;
    font-family: "Arimo", Arial, sans-serif;
    font-weight: 700;
    color: var(--ink);
    font-size: 18px;
    letter-spacing: 0.1px;
    white-space: nowrap;
  }
  .brand-mark {
    width: 12px; height: 12px;
    background: var(--brand-blue);
    flex: none;
  }
  .brand-tagline {
    margin-top: 4px;
    font-family: "Cinzel", Georgia, serif;
    font-size: 7px;
    letter-spacing: 0.3px;
    color: var(--ink-soft);
    text-transform: uppercase;
    white-space: nowrap;
  }
  .front-divider {
    position: absolute;
    left: 256px; top: 50px;
    width: 1px; height: 170px;
    background: linear-gradient(to bottom, transparent, var(--divider) 30%, var(--brand-blue) 100%);
  }
  .contact {
    position: absolute;
    left: 272px; top: 58px;
    right: 22px;
  }
  .contact__name {
    font-weight: 700;
    font-size: 16px;
    color: var(--name-blue);
    letter-spacing: 0.3px;
    white-space: nowrap;
  }
  .contact__role {
    margin-top: 7px;
    font-size: 11px;
    line-height: 1.9;
    color: var(--ink-soft);
  }
  .contact__lines {
    margin-top: 18px;
    list-style: none;
    font-size: 10.5px;
    color: var(--ink);
  }
  .contact__lines li { display: flex; align-items: center; gap: 7px; line-height: 2; white-space: nowrap; }
  .contact__lines svg { width: 12px; height: 12px; fill: var(--brand-blue); flex: none; }
  .front-band {
    position: absolute;
    left: 0; right: 0; bottom: 0;
    height: 34px;
    background: linear-gradient(to bottom, #3a70c8, var(--brand-blue));
    border-top: 3px solid #3a3d45;
    display: flex; align-items: center; justify-content: center;
  }
  .front-band__url {
    color: #dfe8f7;
    font-size: 11px;
    letter-spacing: 2.4px;
  }

  /* back */
  .back-brand {
    position: absolute;
    inset: 0;
    display: flex; flex-direction: column; align-items: center; justify-content: center;
  }
  .back-brand .brand-name { font-size: 34px; color: var(--silver); gap: 14px; }
  .back-brand .brand-mark { width: 24px; height: 24px; }
  .back-brand .brand-tagline { font-size: 13px; color: var(--silver); padding-left: 38px; margin-top: 8px; letter-spacing: 1.6px; }
</style>
</head>
<body>
  <section class="card card--front" aria-label="Business card front">
    <div class="front-brand">
      <div class="brand-name"><span class="brand-mark"></span>Whitcombe Advisors</div>
      <div class="brand-tagline">Small Business Accounting and Taxes</div>
    </div>
    <div class="front-divider"></div>
    <div class="contact">
      <div class="contact__name">Gerald Whitcombe</div>
      <div class="contact__role">President<br>Certified Public Accountant</div>
      <ul class="contact__lines">
        <li>
          <svg viewBox="0 0 24 24" aria-hidden="true"><path d="M6.6 10.8a15.1 15.1 0 0 0 6.6 6.6l2.2-2.2c.3-.3.7-.4 1-.2 1.1.4 2.3.6 3.6.6.6 0 1 .4 1 1V20c0 .6-.4 1-1 1A17 17 0 0 1 3 4c0-.6.4-1 1-1h3.5c.6 0 1 .4 1 1 0 1.3.2 2.5.6 3.6.1.3 0 .7-.2 1z"/></svg>
          (555) 417-2863
        </li>
        <li>
          <svg viewBox="0 0 24 24" aria-hidden="true"><path d="M2 5h20v14H2z M2 5l10 8 10-8" fill="var(--brand-blue)" stroke="#fff" stroke-width="1.5"/></svg>
          GWhitcombe@WhitcombeAdvisors.example
        </li>
      </ul>
    </div>
    <div class="front-band"><span class="front-band__url">www.WhitcombeAdvisors.example</span></div>
  </section>

  <section class="card card--back" aria-label="Business card back">
    <div class="back-brand">
      <div class="brand-name"><span class="brand-mark"></span>Whitcombe Advisors</div>
      <div class="brand-tagline">Small Business Accounting and Taxes</div>
    </div>
  </section>
</body>
</html>
```